Building company buisness cards

We are looking for a sharp modern new look for our business cards.
We are a New Zealand based company that specialises in house and land packages.
We have attached a photo of the current logo and would like to see if it can be improved somehow if needed.
We are open to any colours but we have chosen green at this stage.
Feel free to change the font and make the logo smarter looking.
Play with the colours and see what looks best.

We want a card that looks so good know one will want to throw it away!

Target Market(s)

Home buyers

Industry/Entity Type

Building

Contact Information for Business Card

Dorian Keswick
0217392604
dkeswick@tidewellhomecraft.co.nz
tidewellhomecraft.co.nz

Font styles to use
Serif
Sans Serif

Colors

Designer to choose colors to be used in the design.

Requirements
Must have
• Logo and company name on one side, details on the other side
Nice to have
• Color codes for the original green are HEX #4a8028, RGB(74,128,40), CMYK(42,0,69,50)
• Round corners, Raised and/or spot UV

```html
<!DOCTYPE html>
<html lang="en">
<head>
<meta charset="utf-8">
<title>Tidewell Homecraft – Business Cards</title>
<link href="https://fonts.googleapis.com/css2?family=Montserrat:wght@400;500;800&display=swap" rel="stylesheet">
<style>
  :root {
    --backdrop: #2a2a2c;
    --card: #1e1f21;
    --gloss: #3b3c40;
    --ink-light: #f2f2f2;
    --ink-soft: #cfcfcf;
    --rule: #55575b;
  }
  * { margin: 0; padding: 0; box-sizing: border-box; }
  html, body {
    width: 1200px; height: 800px; overflow: hidden;
    background: var(--backdrop);
    font-family: "Montserrat", sans-serif;
  }
  .stage {
    position: relative; width: 1200px; height: 800px;
    display: flex; align-items: center; justify-content: center; gap: 60px;
  }
  .card {
    position: relative;
    width: 500px; height: 286px;
    background: var(--card);
    border-radius: 10px;
    box-shadow: 0 18px 40px rgba(0,0,0,.45);
    overflow: hidden;
  }
  /* Front */
  .card--front {
    display: flex; flex-direction: column; align-items: center; justify-content: center;
  }
  .brand {
    display: flex; align-items: center; gap: 14px;
  }
  .brand__mark {
    width: 34px; height: 34px; background: var(--gloss); border-radius: 4px;
  }
  .brand__name {
    font-weight: 800; color: var(--gloss); line-height: .95; letter-spacing: -.5px;
  }
  .brand__name .line-top { display: block; font-size: 30px; }
  .brand__name .line-bottom { display: block; font-size: 42px; }
  .front__rule {
    width: 120px; height: 1px; background: var(--rule); margin: 18px 0 12px;
  }
  .front__web {
    font-size: 13px; font-weight: 500; color: var(--ink-light); letter-spacing: .3px;
  }
  /* Back */
  .card--back .details {
    position: absolute; left: 210px; top: 40px; right: 24px;
    color: var(--ink-light);
  }
  .details__company {
    font-weight: 800; line-height: .95; letter-spacing: -.3px;
  }
  .details__company .line-top { display: block; font-size: 22px; }
  .details__company .line-bottom { display: block; font-size: 30px; }
  .details__rule {
    width: 100px; height: 1px; background: var(--rule); margin: 14px 0 12px;
  }
  .details__person { font-size: 19px; font-weight: 500; margin-bottom: 12px; }
  .details__line { font-size: 12px; font-weight: 400; color: var(--ink-soft); margin-bottom: 6px; }
  .details__line b { font-weight: 800; color: var(--ink-light); margin-right: 4px; }
</style>
</head>
<body>
  <main class="stage">
    <section class="card card--front" aria-label="Card front">
      <div class="brand">
        <span class="brand__mark"></span>
        <div class="brand__name">
          <span class="line-top">tidewell</span>
          <span class="line-bottom">homecraft.</span>
        </div>
      </div>
      <div class="front__rule"></div>
      <p class="front__web">tidewellhomecraft.co.nz</p>
    </section>

    <section class="card card--back" aria-label="Card back">
      <div class="details">
        <div class="details__company">
          <span class="line-top">tidewell</span>
          <span class="line-bottom">homecraft.</span>
        </div>
        <div class="details__rule"></div>
        <p class="details__person">Dorian Keswick</p>
        <p class="details__line"><b>P:</b>0217392604</p>
        <p class="details__line"><b>E:</b>dkeswick@tidewellhomecraft.co.nz</p>
        <p class="details__line">tidewellhomecraft.co.nz</p>
      </div>
    </section>
  </main>
</body>
</html>
```